Flyer Design Print Ad for Clothing Store

We are a modest women's clothing store. We are looking for a print ad 90*134 mm that is attention grabbing and can serve as a template for us going forward. We cannot use pictures of actual women. We need it to include our logo, store hours, physical address, website, phone number. We would use this template and change the call to action as necessary e. g. BOGO Sale, 30% off, flash sale, summer sale etc. Our colors are black and white and our fonts are Bodoni sans and Athens.

Target Market(s)

Women from teen to age 70

Industry/Entity Type

Women's clothing

Font styles to use
Other font styles liked:
• Athens, Bodoni Sans

Requirements
Must have
• Our, logo, phone number, website, address and store hours
Nice to have
• I'd like something that's not just our flat logo but something that will make someone pause to look
Should not have
• Pictures of women

```html
<!DOCTYPE html>
<html lang="en">
<head>
<meta charset="utf-8">
<title>Veranelle – BOGO Sale Flyer</title>
<link href="https://fonts.googleapis.com/css2?family=Josefin+Sans:wght@400;600&display=swap" rel="stylesheet">
<style>
  :root {
    --ink: #101722;
    --paper: #ffffff;
    --rule: rgba(255,255,255,0.85);
    --photo-top: #d9d4cc;
    --photo-mid: #b9c3cc;
    --photo-bottom: #ece9e4;
  }
  html, body { margin: 0; padding: 0; overflow: hidden; background: #9a9a9a; }
  .flyer {
    position: relative;
    width: 900px; height: 1200px;
    background: var(--ink);
    color: var(--paper);
    font-family: "Josefin Sans", sans-serif;
    overflow: hidden;
  }
  .flyer-shapes { position: absolute; inset: 0; width: 900px; height: 1200px; }
  .line { position: absolute; left: 0; width: 900px; text-align: center; line-height: 1; }
  .brand-name { top: 182px; font-size: 38px; letter-spacing: 10px; font-weight: 600; }
  .offer-title { top: 566px; font-size: 44px; font-weight: 400; letter-spacing: 1px; }
  .offer-sub { top: 604px; font-size: 24px; letter-spacing: 1px; }
  .offer-rule { position: absolute; left: 436px; top: 634px; width: 28px; height: 1px; background: var(--rule); }
  .offer-discount { top: 640px; font-size: 46px; }
  .offer-discount small { font-size: 24px; letter-spacing: 2px; margin-left: 6px; }
  .hours-title { top: 778px; font-size: 34px; font-weight: 600; letter-spacing: 1px; line-height: 33px; }
  .hours-row {
    position: absolute; left: 115px; top: 860px; width: 670px; height: 44px;
    border-bottom: 1px solid var(--rule);
    font-size: 24px; letter-spacing: 2px;
  }
  .hours-day, .hours-time { position: absolute; top: 16px; line-height: 1; }
  .hours-day { right: 355px; }
  .hours-time { left: 350px; }
  .hours-divider { position: absolute; left: 335px; top: 0; width: 1px; height: 44px; background: var(--rule); }
  .phone-pill {
    position: absolute; left: 259px; top: 940px; width: 382px; height: 52px;
    background: var(--paper); color: var(--ink); border-radius: 26px;
    text-align: center; font-size: 38px; letter-spacing: 3px; line-height: 58px;
  }
  .icon { position: absolute; left: 441px; width: 18px; height: 18px; }
  .icon-globe { top: 1019px; }
  .icon-pin { top: 1089px; }
  .website { top: 1045px; font-size: 22px; letter-spacing: 2px; }
  .contact-rule { position: absolute; left: 420px; top: 1077px; width: 60px; height: 1px; background: var(--rule); }
  .address { top: 1113px; font-size: 24px; letter-spacing: 2px; line-height: 30px; }
</style>
</head>
<body>
<main class="flyer">
  <svg class="flyer-shapes" viewBox="0 0 850 1268" preserveAspectRatio="none" aria-hidden="false">
    <defs>
      <linearGradient id="store-photo-tone" x1="0" y1="0" x2="0" y2="1">
        <stop offset="0" stop-color="var(--photo-top)"/>
        <stop offset="0.5" stop-color="var(--photo-mid)"/>
        <stop offset="1" stop-color="var(--photo-bottom)"/>
      </linearGradient>
    </defs>
    <g class="frame-rules" stroke="#ffffff" stroke-width="1.5" fill="none">
      <line x1="0" y1="515" x2="250" y2="515"/>
      <line x1="600" y1="515" x2="850" y2="515"/>
      <path d="M190 265 L330 265 Q390 268 425 338 Q460 268 520 265 L660 265 Q675 265 675 280 L675 410 Q672 480 600 515 Q672 550 675 620 L675 750 Q675 765 660 765 L190 765 Q175 765 175 750 L175 620 Q178 550 250 515 Q178 480 175 410 L175 280 Q175 265 190 265 Z"/>
    </g>
    <path class="store-photo" role="img" aria-label="Photo of a bright boutique interior with dresses and blouses on hanging rails"
      fill="url(#store-photo-tone)"
      d="M200 279 L330 279 Q385 282 425 355 Q465 282 520 279 L650 279 Q660 279 660 289 L660 415 Q655 485 585 515 Q655 545 660 610 L660 740 Q660 750 650 750 L200 750 Q190 750 190 740 L190 610 Q195 545 265 515 Q195 485 190 415 L190 289 Q190 279 200 279 Z"/>
    <path class="offer-badge" fill="#101722"
      d="M325 553 L390 553 Q415 553 425 575 Q435 553 460 553 L525 553 Q538 553 538 566 L538 640 Q538 660 520 665 Q538 670 538 690 L538 765 Q538 778 525 778 L460 778 Q435 778 425 758 Q415 778 390 778 L325 778 Q312 778 312 765 L312 690 Q312 670 330 665 Q312 660 312 640 L312 566 Q312 553 325 553 Z"/>
  </svg>

  <div class="line brand-name">VERANELLE</div>

  <div class="line offer-title">BOGO</div>
  <div class="line offer-sub">Sale</div>
  <div class="offer-rule"></div>
  <div class="line offer-discount">30%<small>OFF</small></div>

  <div class="line hours-title">Store<br>Opening Hours</div>
  <div class="hours-row">
    <span class="hours-day">Monday- Thursday</span>
    <span class="hours-divider"></span>
    <span class="hours-time">09.30am - 10.30pm</span>
  </div>

  <div class="phone-pill">077-5550142</div>

  <svg class="icon icon-globe" viewBox="0 0 18 18" fill="none" stroke="#fff" stroke-width="1.2">
    <circle cx="9" cy="9" r="7.5"/>
    <ellipse cx="9" cy="9" rx="3.2" ry="7.5"/>
    <line x1="1.5" y1="9" x2="16.5" y2="9"/>
    <line x1="3" y1="5" x2="15" y2="5"/>
    <line x1="3" y1="13" x2="15" y2="13"/>
  </svg>
  <div class="line website">Veranelle.co.il</div>
  <div class="contact-rule"></div>
  <svg class="icon icon-pin" viewBox="0 0 18 18" fill="none" stroke="#fff" stroke-width="1.2">
    <path d="M9 17 C5 12 3.5 9.5 3.5 7 A5.5 5.5 0 0 1 14.5 7 C14.5 9.5 13 12 9 17 Z"/>
    <circle cx="9" cy="7" r="2"/>
  </svg>
  <div class="line address">Alder Shopping Center<br>Nof Hadar, Jerusalem, Israel</div>
</main>
</body>
</html>
```